Flyer-Design für Pfandhaus
Zielgruppe
Wir vergeben Pfandkrediten für
- Gold und Silberschmuck
- Goldbarren und Münzen
- Technik ( Spielkonsolen , Kameras , Laptop , Smartphones , Tablets )
- Hochwertiges Werkzeug ( Vorlo , Teruno , Grenz Werkpro etc.)
Desweiteren wird Gold angekauft in allen Arten ( Altgold , Bruchgold , Zahngold , Barren , Münzen , Schmuck und Uhren )
Aufgabenstellung
Wichtig sind die Beiden Hauptsachen
Pfandhaus - Goldankauf würde das gerne mit ca. 2 Bilder etwas untermalen.
Sie könne unter meiner Homepage www.leihhaus-mebold.de mein Farbkonzept erkennen bin aber daran nicht fix gebunden wenn es andere Kreative Ideen vorkommen.
Ich möchte die Flyer gerne verteilen lassen als Beilage oder direktverteilung soll also etwas auffallen.

```html
<!DOCTYPE html>
<html lang="de">
<head>
<meta charset="utf-8">
<title>Marius Mebold Pfandkredit – Flyer</title>
<link rel="stylesheet" href="https://fonts.googleapis.com/css2?family=Barlow:wght@300;400;500;600;700&display=swap">
<style>
  :root {
    --ink: #2b2b2b;
    --night: #212222;
    --charcoal: #2e2e2e;
    --gold-light: #f6e597;
    --gold-mid: #e9c467;
    --gold-deep: #d4952e;
    --gold-text: #f0d78a;
    --paper: #ffffff;
  }
  * { margin: 0; padding: 0; box-sizing: border-box; }
  html, body { width: 841px; height: 1200px; overflow: hidden; background: var(--charcoal); }
  .flyer {
    position: relative; width: 841px; height: 1200px; overflow: hidden;
    background: var(--charcoal);
    font-family: "Barlow", sans-serif;
  }
  .backdrop { position: absolute; inset: 0; }
  .abs { position: absolute; }

  .brand {
    left: 40px; top: 37px; width: 253px; height: 124px;
    display: flex; flex-direction: column; align-items: center; justify-content: center;
    color: var(--gold-mid); font-weight: 400; font-size: 30px; line-height: 1.1; text-align: center;
  }
  .brand small { font-size: 22px; }

  .headline-kicker {
    right: 25px; top: 50px; color: var(--paper);
    font-weight: 300; font-size: 38px; letter-spacing: 1px; white-space: nowrap;
  }
  .headline-main {
    right: 25px; top: 92px; color: var(--gold-mid);
    font-weight: 300; font-size: 74px; letter-spacing: 2px; line-height: 1; white-space: nowrap;
  }

  .claim {
    left: 49px; top: 242px; color: var(--ink);
    font-weight: 600; font-size: 52px; line-height: 0.86; letter-spacing: 1px;
  }
  .pawn-list {
    left: 49px; top: 377px; color: var(--ink);
    font-weight: 500; font-size: 21px; line-height: 28px;
  }

  .seal-label {
    left: 50px; top: 532px; width: 160px; text-align: center; color: var(--ink);
  }
  .seal-label strong { display: block; font-weight: 700; font-size: 52px; line-height: 1; }
  .seal-label span { display: block; font-weight: 400; font-size: 17px; margin-top: 2px; }

  .services {
    right: 66px; top: 498px; text-align: right; color: var(--gold-text);
    font-weight: 500; font-size: 19.5px; line-height: 24.5px;
  }
  .services p + p { margin-top: 24px; }

  .cash-title {
    right: 26px; top: 770px; text-align: right; color: var(--ink);
    font-weight: 600; line-height: 1;
  }
  .cash-title .big { display: block; font-size: 50px; letter-spacing: 1px; }
  .cash-title .sub { display: block; font-size: 37px; letter-spacing: 1px; margin-top: 6px; }

  .gold-list {
    right: 26px; top: 911px; text-align: right; color: var(--ink);
    font-weight: 500; font-size: 21px; line-height: 28px;
  }

  .contact { left: 186px; top: 1004px; list-style: none; }
  .contact li {
    display: flex; align-items: center; height: 46px;
    color: var(--paper); font-weight: 500; font-size: 18px; letter-spacing: 0.5px;
  }
  .contact svg { width: 36px; height: 36px; margin-right: 16px; flex: none; }
</style>
</head>
<body>
<div class="flyer">
  <svg class="backdrop" width="841" height="1200" viewBox="0 0 841 1200" aria-hidden="true">
    <defs>
      <linearGradient id="goldSheen" x1="0" y1="0" x2="1" y2="0.3">
        <stop offset="0" stop-color="#e7c46a"/>
        <stop offset="0.35" stop-color="#f6e597"/>
        <stop offset="0.65" stop-color="#d8982f"/>
        <stop offset="1" stop-color="#f7eaa0"/>
      </linearGradient>
      <linearGradient id="goldBlock" x1="0" y1="0" x2="1" y2="1">
        <stop offset="0" stop-color="#e6bd5c"/>
        <stop offset="0.5" stop-color="#f6e597"/>
        <stop offset="1" stop-color="#e8c267"/>
      </linearGradient>
      <radialGradient id="sealGold" cx="0.4" cy="0.35" r="0.7">
        <stop offset="0" stop-color="#f8e28a"/>
        <stop offset="0.6" stop-color="#e6ad4a"/>
        <stop offset="1" stop-color="#f3d98a"/>
      </radialGradient>
      <linearGradient id="barsTone" x1="0" y1="0" x2="1" y2="1">
        <stop offset="0" stop-color="#5a4a2e"/>
        <stop offset="0.5" stop-color="#b98a3e"/>
        <stop offset="1" stop-color="#6b5330"/>
      </linearGradient>
    </defs>

    <!-- brand frame and header rule -->
    <rect x="40.5" y="37.5" width="253" height="123" fill="none" stroke="var(--gold-mid)" stroke-width="1.5"/>
    <rect x="0" y="180" width="815" height="2" fill="var(--gold-mid)"/>

    <!-- upper gold bands -->
    <polygon points="0,228 841,228 841,321 807,345 0,345" fill="url(#goldSheen)"/>
    <polygon points="0,360 787,360 665,451 0,451" fill="url(#goldSheen)"/>
    <polygon points="841,438 841,466 801,466" fill="url(#goldSheen)"/>

    <!-- trust panel -->
    <rect x="0" y="466" width="841" height="213" fill="var(--night)"/>
    <path d="M130,478 C160,474 190,500 210,520 C230,545 228,590 212,620 C198,650 165,668 128,664 C92,660 56,645 42,610 C30,580 40,540 60,515 C78,493 100,481 130,478 Z" fill="url(#sealGold)"/>
    <circle cx="130" cy="572" r="75" fill="none" stroke="var(--ink)" stroke-width="4"/>

    <!-- lower section -->
    <rect x="0" y="679" width="841" height="521" fill="var(--charcoal)"/>
    <polygon points="0,679 351,679 0,936" fill="url(#barsTone)" role="img" aria-label="Fotofläche: Feingoldbarren in Nahaufnahme"/>
    <polygon points="510,679 593,679 0,1124 0,1056" fill="url(#goldBlock)"/>
    <polygon points="483,762 841,762 841,985 185,985" fill="url(#goldBlock)"/>
    <polygon points="326,880 841,880 841,893 309,893" fill="#3a3a3a"/>
  </svg>

  <div class="abs brand">Marius Mebold<small>Pfandkredit</small></div>

  <div class="abs headline-kicker">HOLEN SIE SICH JETZT IHREN</div>
  <div class="abs headline-main">PFANDKREDIT</div>

  <h1 class="abs claim">SCHNELL UND<br>UNKOMLIZIERT</h1>
  <p class="abs pawn-list">FÜR GOLD UND SILBERSCHMUCK, GOLDBARREN UND<br>MÜNZEN, TECHNIK UND HOCHWERTIGES WERKZEUG</p>

  <div class="abs seal-label"><strong>100%</strong><span>ZUFRIEDENHEIT</span></div>

  <div class="abs services">
    <p>SIE KÖNNEN BEI UNS WERTGEGENSTÄNDE<br>BELEIHEN, ERSTEIGERN, KAUFEN UND VERKAUFEN.</p>
    <p>VON SCHMUCK, UHREN, GOLD UND SILBERWAREN,<br>TECHNISCHEN GERÄTEN, BIS HIN ZU PKWS, LKWS UND<br>ALLE ARTEN VON ZWEIRÄDERN.</p>
  </div>

  <h2 class="abs cash-title"><span class="big">SOFORTIGE</span><span class="sub">BARGELDAUSZAHLUNG</span></h2>
  <p class="abs gold-list">FÜR SCHMUCK, ALTGOLD, MÜNZEN, BRUCHGOLD,<br>BARREN, FEINGOLD, ZAHNGOLD UND SILBER</p>

  <ul class="abs contact">
    <li>
      <svg viewBox="0 0 36 36" aria-hidden="true"><circle cx="18" cy="18" r="16" fill="#2a2a2a" stroke="var(--gold-mid)" stroke-width="2"/><path d="M18,9 a6,6 0 0 1 6,6 c0,4 -6,11 -6,11 s-6,-7 -6,-11 a6,6 0 0 1 6,-6 z" fill="var(--gold-mid)"/><circle cx="18" cy="15" r="2.2" fill="#2a2a2a"/></svg>
      Lindenweg 14, 66113 Musterstadt
    </li>
    <li>
      <svg viewBox="0 0 36 36" aria-hidden="true"><circle cx="18" cy="18" r="16" fill="#2a2a2a" stroke="var(--gold-mid)" stroke-width="2"/><rect x="10" y="12" width="16" height="12" fill="var(--gold-mid)"/><path d="M10,12 L18,19 L26,12" fill="none" stroke="#2a2a2a" stroke-width="1.5"/></svg>
      info@leihhaus-mebold.de
    </li>
    <li>
      <svg viewBox="0 0 36 36" aria-hidden="true"><circle cx="18" cy="18" r="16" fill="#2a2a2a" stroke="var(--gold-mid)" stroke-width="2"/><circle cx="18" cy="18" r="3.5" fill="none" stroke="var(--gold-mid)" stroke-width="1.8"/><path d="M21.5,15 v5 a2.5,2.5 0 0 0 5,0 v-2 a8.5,8.5 0 1 0 -3.5,7" fill="none" stroke="var(--gold-mid)" stroke-width="1.8"/></svg>
      www.leihhaus-mebold.de
    </li>
    <li>
      <svg viewBox="0 0 36 36" aria-hidden="true"><circle cx="18" cy="18" r="16" fill="#2a2a2a" stroke="var(--gold-mid)" stroke-width="2"/><path d="M9,15 c2,-4 16,-4 18,0 l-3,2 l-2,-2 h-8 l-2,2 z" fill="var(--gold-mid)"/><rect x="11" y="18" width="14" height="8" rx="2" fill="var(--gold-mid)"/><circle cx="18" cy="22" r="2" fill="#2a2a2a"/></svg>
      +49 681 55 501 234
    </li>
  </ul>
</div>
</body>
</html>
```